Webdesign für die Korvelt GmbH
Zielgruppe
Beratung • Renovierung • Reparatur • Planung • Bau • Pflege • Wartung im Bereich der Haustechnik
Aufgabenstellung
Bilder nur von bildmoro oder von der Webseite des Kunden nutzen

```html
<!DOCTYPE html>
<html lang="de">
<head>
<meta charset="utf-8">
<title>Korvelt Heizung-Sanitär GmbH</title>
<link href="https://fonts.googleapis.com/css2?family=Poppins:wght@400;500;600;700&family=Roboto:wght@300;400;500&display=swap" rel="stylesheet">
<style>
:root{
  --brand-blue:#1b1fe0;
  --brand-red:#f20a0a;
  --ink:#2b2f3a;
  --muted:#6b6f80;
  --light-bg:#f3f4f8;
  --link-blue:#4255e0;
  --white:#ffffff;
}
*{margin:0;padding:0;box-sizing:border-box}
html,body{width:1200px;height:2927px;overflow:hidden}
body{position:relative;font-family:"Roboto",sans-serif;color:var(--ink);background:var(--white)}
/* header */
.site-header{position:absolute;left:0;top:0;width:1200px;height:93px;background:var(--white)}
.brand{position:absolute;left:160px;top:22px;display:flex;align-items:center;gap:10px}
.brand-mark{width:14px;height:14px;background:var(--brand-red)}
.brand-name{font-family:"Poppins",sans-serif;font-weight:600;font-size:30px;color:var(--brand-blue);letter-spacing:.5px}
.main-nav a{position:absolute;top:42px;font-family:"Roboto",sans-serif;font-weight:500;font-size:11.5px;color:var(--ink);text-decoration:none;white-space:nowrap}
.hotline{position:absolute;left:0;top:0;width:1200px;height:93px}
.hotline-text{position:absolute;left:945px;top:28px;color:var(--white)}
.hotline-text small{display:block;font-size:10px;font-weight:500}
.hotline-text strong{display:block;font-family:"Poppins",sans-serif;font-weight:500;font-size:18px;margin-top:1px}
/* hero */
.hero{position:absolute;left:0;top:93px;width:1200px;height:535px;background:linear-gradient(120deg,#6f70a6 0%,#5a5c99 45%,#7d8fc4 70%,#5b5d97 100%)}
.hero-kicker{position:absolute;left:160px;top:142px;font-size:12px;line-height:14px;color:var(--white)}
.hero-title{position:absolute;left:160px;top:160px;font-family:"Poppins",sans-serif;font-weight:700;font-size:26px;line-height:32px;color:var(--white)}
.hero-text{position:absolute;left:160px;top:200px;width:405px;font-size:12px;line-height:18px;color:var(--white)}
.hero-btn{position:absolute;left:160px;top:261px;width:136px;height:36px;border:1px solid var(--white);color:var(--white);font-size:11px;text-align:center;line-height:34px}
.dot{position:absolute;top:498px;width:37px;height:3px;background:var(--white)}
.dot.active{background:var(--brand-red)}
/* services */
.services{position:absolute;left:0;top:628px;width:1200px;height:593px;background:var(--light-bg)}
.section-title{position:absolute;left:160px;top:38px;font-weight:300;font-size:22px;line-height:26px;color:var(--ink);letter-spacing:.3px}
.section-lead{position:absolute;left:160px;top:72px;width:870px;font-size:12.5px;line-height:22.5px;color:var(--muted)}
.divider{position:absolute;left:160px;top:154px;width:878px;height:1px;background:#dcdde5}
.card{position:absolute;top:198px;width:203px;height:316px;background:var(--white);box-shadow:0 1px 3px rgba(0,0,0,.08)}
.card-img{width:203px;height:142px}
.card h3{position:absolute;left:15px;top:158px;font-size:12.5px;font-weight:500;color:var(--ink)}
.card ul{position:absolute;left:15px;top:183px;list-style:none;font-size:10.5px;line-height:18px;color:var(--muted)}
.card .more{position:absolute;left:15px;top:284px;font-size:9.5px;font-weight:500;color:var(--brand-red)}
/* about */
.about{position:absolute;left:0;top:1221px;width:1200px;height:466px;background:var(--white)}
.about-img{position:absolute;left:160px;top:102px;width:383px;height:330px;background:linear-gradient(180deg,#cfd8e8 0%,#e9ecf2 40%,#b23c3c 60%,#3d4f9a 80%,#a9a59c 100%)}
.frame{position:absolute;border:1px solid rgba(255,255,255,.8)}
.kicker{position:absolute;left:610px;top:133px;font-size:12px;color:var(--brand-blue)}
.about h2{position:absolute;left:610px;top:153px;font-weight:400;font-size:22px;color:var(--ink)}
.about p{position:absolute;left:610px;top:195px;width:430px;font-size:11px;line-height:21px;color:var(--muted)}
.btn-outline{position:absolute;left:608px;top:345px;width:135px;height:36px;border:1px solid #9a9cab;box-shadow:0 1px 3px rgba(0,0,0,.15);font-size:12px;text-align:center;line-height:34px;color:var(--ink)}
/* reasons */
.reasons{position:absolute;left:0;top:1687px;width:1200px;height:629px;background:var(--light-bg)}
.reasons h2{position:absolute;left:160px;top:70px;font-weight:500;font-size:22px;color:var(--ink)}
.reason{position:absolute;width:230px}
.reason h4{font-family:"Poppins",sans-serif;font-weight:500;font-size:13px;color:var(--ink)}
.reason p{margin-top:20px;font-family:"Poppins",sans-serif;font-size:11.5px;line-height:19.5px;color:var(--muted)}
.reasons-img{position:absolute;left:734px;top:159px;width:303px;height:356px;background:linear-gradient(180deg,#e3e6ef 0%,#3c50a8 45%,#7d8397 75%,#e8eaee 100%)}
/* cta */
.cta{position:absolute;left:0;top:2316px;width:1200px;height:289px;background:linear-gradient(90deg,#56578f,#5d5e98 50%,#56578f)}
.cta h2{position:absolute;left:0;top:70px;width:1200px;text-align:center;font-weight:500;font-size:27px;line-height:35px;color:var(--white)}
.cta-call{position:absolute;left:0;top:180px;width:1200px;text-align:center;color:var(--white)}
.cta-call span{display:block;font-family:"Poppins",sans-serif;font-size:16px}
.cta-call strong{display:inline-flex;align-items:center;gap:8px;font-family:"Poppins",sans-serif;font-weight:400;font-size:25px}
/* footer */
.site-footer{position:absolute;left:0;top:2605px;width:1200px;height:275px;background:var(--white)}
.footer-title{position:absolute;top:68px;font-size:18px;font-weight:400;color:var(--link-blue)}
.footer-col{position:absolute;top:110px;font-size:10.5px;line-height:19px;color:var(--ink);list-style:none}
.footer-brand{position:absolute;left:767px;top:78px;display:flex;align-items:center;gap:12px}
.footer-brand .brand-name{font-size:46px}
.footer-brand .brand-mark{width:22px;height:22px}
.bottom-bar{position:absolute;left:0;top:2880px;width:1200px;height:47px;background:var(--brand-red);color:var(--white);font-size:10.5px}
.bottom-bar .copy{position:absolute;left:160px;top:17px}
.bottom-bar .legal{position:absolute;right:162px;top:17px}
</style>
</head>
<body>

<header class="site-header">
  <div class="brand"><span class="brand-name">KORVELT</span><span class="brand-mark"></span></div>
  <nav class="main-nav">
    <a style="left:498px">STARTSEITE</a>
    <a style="left:577px">ÜBER UNS</a>
    <a style="left:649px">LEISTUNGEN</a>
    <a style="left:735px">SERVICETEAM</a>
    <a style="left:833px">REFERENZEN</a>
  </nav>
  <svg class="hotline" viewBox="0 0 1200 93"><polygon points="940,0 1200,0 1200,93 911,93" fill="#f20a0a"/></svg>
  <div class="hotline-text"><small>FREIER BERATER</small><strong>01234-5678-0</strong></div>
</header>

<section class="hero" role="img" aria-label="Foto einer Poolanlage mit gepflastertem Rand, blau eingefärbt">
  <div class="hero-kicker">WIR PFLEGEN UND WARTEN</div>
  <div class="hero-title">POOLANLAGE</div>
  <p class="hero-text">alle Heizungs-, Lüftungs- und Sanitäranlagen und bieten Ihnen darüber hinaus Wartungsverträge für alle genannten Bereiche</p>
  <div class="hero-btn">WEITERLESEN</div>
  <span class="dot active" style="left:160px"></span>
  <span class="dot" style="left:207px"></span>
  <span class="dot" style="left:252px"></span>
</section>

<section class="services">
  <h2 class="section-title">LEISTUNGEN DER KORVELT HEIZUNG-SANITÄR GMBH</h2>
  <p class="section-lead">Wenn Sie einen zuverlässigen Partner für die Erledigung Ihrer Aufträge suchen, Wert auf Kreativität und Freundlichkeit legen, dann sind Sie bei uns an der richtigen Stelle. Vom ersten Beratungsgespräch bis zur Übergabe der fertiggestellten Leistung, sollten Sie, wie viele Kunden vor Ihnen, gute Erfahrungen mit uns machen.</p>
  <div class="divider"></div>

  <article class="card" style="left:160px">
    <div class="card-img" role="img" aria-label="Foto eines Hausdachs mit Solaranlage" style="background:linear-gradient(180deg,#c98b4a,#3c4150 55%,#8a6a4f)"></div>
    <h3>WÄRME</h3>
    <ul><li>Blockheizkraftwerk</li><li>Wärmepumpen</li><li>Solaranlagen</li><li>Holz</li><li>Energiespartips</li></ul>
    <span class="more">WEITERLESEN &rsaquo;</span>
  </article>
  <article class="card" style="left:385px">
    <div class="card-img" role="img" aria-label="Foto von Händen mit Werkzeug an einem Heizungsverteiler" style="background:linear-gradient(135deg,#e8e2dc,#c9a66b 50%,#e34a3a)"></div>
    <h3>WASSER</h3>
    <ul><li>Sanitärtechnik</li><li>Bäder</li><li>Pool</li><li>Regenwasser</li></ul>
    <span class="more">WEITERLESEN &rsaquo;</span>
  </article>
  <article class="card" style="left:610px">
    <div class="card-img" role="img" aria-label="Foto einer Klima- und Lüftungsanlage auf einem Dach" style="background:linear-gradient(135deg,#dfe3e8,#9aa3ad 50%,#5b7fb8)"></div>
    <h3>LUFT</h3>
    <ul><li>Kontrollierte Wohnraumlüftung</li><li>Klima</li><li>Zentrale Staubsauganlagen</li></ul>
    <span class="more">WEITERLESEN &rsaquo;</span>
  </article>
  <article class="card" style="left:835px">
    <div class="card-img" role="img" aria-label="Foto eines Dachdeckers auf einem Ziegeldach" style="background:linear-gradient(180deg,#b56a4e,#d89a7e 45%,#f2eeea)"></div>
    <h3>DACH und Service</h3>
    <ul><li>Dachklempner</li><li>Photovoltaik</li><li>Thermische Solaranlagen</li><li>Wartung</li><li>Gascheck</li></ul>
    <span class="more">WEITERLESEN &rsaquo;</span>
  </article>
</section>

<section class="about">
  <div class="about-img" role="img" aria-label="Gruppenfoto des Teams vor dem Firmengebäude">
    <div class="frame" style="left:14px;top:13px;width:355px;height:304px"></div>
  </div>
  <div class="kicker">ÜBER UNS</div>
  <h2>SEHR GEEHRTE DAMEN UND HERREN</h2>
  <p>Angefangen hat alles ganz klein - damals 1949. Weil es in Rosenau, dort lebte Installateur- und Klempnermeister Erich Korvelt mit Frau und Kind, schon einige Klempnereien gab, beschloss der Familienrat, sich neue Kundschaft zu suchen. Eine geeignete Werkstatt wurde auf der Bergstraße 37 in Talbach gefunden. Dort gründete mein Vater Erich Korvelt am 01. Juni 1949 einen Installations- und Klempnerbetrieb.</p>
  <div class="btn-outline">Weiterlesen</div>
</section>

<section class="reasons">
  <h2>ES SOLLTE EINEN GRUND GEBEN, UNS ZU WÄHLEN!</h2>
  <div class="reason" style="left:160px;top:158px"><h4>Erfahrene Ingenieure</h4><p>Lorem ipsum dolor sit amet, consectetur adipiscing elit, sed do eiusmod tempor incididunt.</p></div>
  <div class="reason" style="left:433px;top:158px"><h4>Bester Service</h4><p>Lorem ipsum dolor sit amet, consectetur adipiscing elit, sed do eiusmod tempor incididunt.</p></div>
  <div class="reason" style="left:160px;top:293px"><h4>Kostenloses Angebot</h4><p>Lorem ipsum dolor sit amet, consectetur adipiscing elit, sed do eiusmod tempor incididunt.</p></div>
  <div class="reason" style="left:433px;top:293px"><h4>Pünktlich arbeiten</h4><p>Lorem ipsum dolor sit amet, consectetur adipiscing elit, sed do eiusmod tempor incididunt.</p></div>
  <div class="reason" style="left:160px;top:428px"><h4>Kundendienst</h4><p>Lorem ipsum dolor sit amet, consectetur adipiscing elit, sed do eiusmod tempor incididunt.</p></div>
  <div class="reason" style="left:433px;top:428px"><h4>100% garantiert</h4><p>Lorem ipsum dolor sit amet, consectetur adipiscing elit, sed do eiusmod tempor incididunt.</p></div>
  <div class="reasons-img" role="img" aria-label="Foto zweier Männer vor dem Firmengebäude zum 50-jährigen Jubiläum">
    <div class="frame" style="left:16px;top:16px;width:271px;height:324px"></div>
  </div>
</section>

<section class="cta">
  <h2>Alle Heizungs-, Lüftungs- und Sanitäranlagen und bieten Ihnen<br>darüber hinaus Wartungsverträge für alle genannten Bereiche</h2>
  <div class="cta-call">
    <span>Rufen Sie jetzt kostenlos an</span>
    <strong>
      <svg width="22" height="22" viewBox="0 0 24 24" fill="none" stroke="#fff" stroke-width="1.6" stroke-linejoin="round"><path d="M5 3h4l2 5-2.5 1.5a11 11 0 0 0 6 6L16 13l5 2v4a2 2 0 0 1-2 2A16 16 0 0 1 3 5a2 2 0 0 1 2-2z"/></svg>
      01234-5678-0
    </strong>
  </div>
</section>

<footer class="site-footer">
  <h3 class="footer-title" style="left:160px">KONTAKT</h3>
  <ul class="footer-col" style="left:160px"><li>Telefon:01234-5678-0</li><li>Fax:01234-5678-39</li><li>info@korvelt-gmbh.example</li></ul>
  <ul class="footer-col" style="left:318px;line-height:17px"><li>Korvelt Heizung-Sanitär GmbH</li><li>Lindenweg 14</li><li>00000 Talbach / Erzg.</li></ul>
  <h3 class="footer-title" style="left:555px">Schnelle Navigation</h3>
  <ul class="footer-col" style="left:555px;line-height:18px"><li>Startseite</li><li>Über uns</li><li>Leistungen</li><li>Serviceteam</li><li>Referenzen</li></ul>
  <div class="footer-brand"><span class="brand-name">KORVELT</span><span class="brand-mark"></span></div>
</footer>

<div class="bottom-bar">
  <span class="copy">Korvelt Heizung-Sanitär GmbH © 2019</span>
  <span class="legal">Impressum | Kontakt | Datenschutz</span>
</div>

</body>
</html>
```